Dance School poster for end of year dance concert for mainly young girls.

We need an A3 portrait poster for our end of year concert.
Designs are attached of posters from previous 2 years as a reference only.
The theme of our concert this year is "Let's Dance" which we want to convey a general feel of energy & fun with dance.
Dance styles in the concert include Jazz & Hip Hop.
Bright colors are preferred in the design.

Target Market(s)

The concert is attended by several hundred family & friends

Industry/Entity Type

Dance Studio

Requirements
Must have
• Must have
• Let's Dance
• BRK logo (file supplied)
• 'The Maribel Crowe Dancers' (font is Mistral)
• Date of the concert: Saturday 14th November 2015
• Pellow Theatre, Saint Fenwick College Dalebrook
Nice to have
• We like clean design with no cluttered imagery.

```html
<!DOCTYPE html>
<html lang="en">
<head>
<meta charset="utf-8">
<title>Let's Dance – The Maribel Crowe Dancers</title>
<link rel="stylesheet" href="https://fonts.googleapis.com/css2?family=Codystar:wght@400&family=Oswald:wght@500;600&display=swap">
<style>
  :root {
    --ink: #000000;
    --pink: #ec1f8c;
    --white: #ffffff;
  }
  * { margin: 0; padding: 0; box-sizing: border-box; }
  html, body { width: 849px; height: 1200px; overflow: hidden; background: var(--ink); }
  .poster {
    position: relative;
    width: 849px;
    height: 1200px;
    background: var(--ink);
    overflow: hidden;
    font-family: "Oswald", "Arial Narrow", sans-serif;
  }
  .frame {
    position: absolute;
    left: 62px; top: 28px;
    width: 739px; height: 1132px;
    border: 3px solid var(--pink);
  }
  .dancers-photo {
    position: absolute;
    left: 300px; top: 180px;
    width: 549px; height: 1000px;
    background:
      radial-gradient(ellipse 45% 30% at 55% 55%, rgba(236,31,140,0.55), transparent 70%),
      radial-gradient(ellipse 40% 45% at 60% 40%, #3a2a26 0%, #1a1312 55%, transparent 80%);
  }
  .brand {
    position: absolute;
    right: 30px; top: 20px;
    display: flex; align-items: center; gap: 12px;
    padding: 10px 16px;
    background: var(--ink);
  }
  .brand-dot { width: 26px; height: 26px; border-radius: 50%; background: var(--pink); }
  .brand-name {
    font-weight: 600; font-size: 52px; line-height: 1;
    color: var(--white); letter-spacing: 2px;
  }
  .headline {
    position: absolute;
    left: 112px; top: 168px;
    font-family: "Codystar", "Courier New", monospace;
    font-weight: 400;
    font-size: 100px; line-height: 84px;
    color: var(--pink);
    text-transform: uppercase;
    -webkit-text-stroke: 2px var(--pink);
    transform: scaleY(1.3);
    transform-origin: left top;
  }
  .details {
    position: absolute;
    left: 84px; top: 758px;
    width: 580px;
    text-align: center;
    color: var(--white);
    font-weight: 500; font-size: 36px; line-height: 60px;
    text-transform: uppercase; letter-spacing: 1px;
  }
  .school-name {
    position: absolute;
    left: 99px; top: 1122px;
    width: 424px; height: 60px;
    background: var(--pink);
    color: var(--white);
    display: flex; align-items: center; justify-content: center;
    font-weight: 500; font-size: 26px; letter-spacing: 1px;
    text-transform: uppercase;
  }
</style>
</head>
<body>
  <main class="poster">
    <div class="frame"></div>
    <div class="dancers-photo" role="img" aria-label="Photograph of a male and female dancer in a dramatic dip, she in a pink fringed dress, he in a hat and waistcoat"></div>
    <div class="brand">
      <span class="brand-dot"></span>
      <span class="brand-name">BRK</span>
    </div>
    <h1 class="headline">Let's<br>Dance</h1>
    <p class="details">
      Saturday<br>
      14th November 2015<br>
      Pellow Theatre<br>
      Saint Fenwick College Dalebrook
    </p>
    <div class="school-name">The Maribel Crowe Dancers</div>
  </main>
</body>
</html>
```